Cover Design Brief – Prayer Book (Modern Revision)

Design a new, modern, high-quality book cover that reflects the essence of the original version. The updated cover should feel contemporary yet familiar, appealing to both younger and older readers, while evoking a sense of spiritual depth, calm, and authenticity.

1. Visual Reference to the Original Cover
Continuity:
Retain visual elements such as the color palette, central motifs (eg, geometric patterns, Islamic ornaments, or a symbolic figure), and overall structure from the original cover.

Recognition:
Readers familiar with the old cover should instantly recognize the book but be pleasantly surprised by the refined, modern look.

2. Style & Mood
Modern Islamic design, minimalist and clean rather than ornate.

Spiritual, calming, elegant – avoid overly bright or flashy visuals.

Subtle use of Islamic motifs, possibly a decorative Arabic calligraphy word like ṣalāh (صلاة) to enrich the theme.

3. Suggested Color Palette
Deep blue, teal, petrol green, olive, sand tones, or midnight blue with accents of gold – depending on the original cover scheme.

Avoid neon or loud colors.

If gold or silver is used, it should be subtle and classy (eg, foil stamping or embossing, not digital effects).

4. Typography
A modern serif font for the main title is welcome, but it should be clean and elegant.

Subtitles should use a clear, legible font.

If the title includes Arabic text, it should be displayed in tasteful classical calligraphy or a stylized script.

5. Back Cover
Will include a brief description text (to be provided later).

Clean layout, optionally with a small publisher logo.

Possibly a short quote or ḥadīth in Arabic (with or without translation) to complement the design.

6. Target Audience
German-speaking Muslims, male and female, ages 15+

Suitable for both beginners and advanced practitioners of the prayer

Designed as a long-term spiritual companion and a thoughtful gift

```html
<!DOCTYPE html>
<html lang="de">
<head>
<meta charset="utf-8">
<title>Ṣalāh – Das Gebet im Islam</title>
<link rel="stylesheet" href="https://fonts.googleapis.com/css2?family=EB+Garamond:ital,wght@0,400;0,500;0,600;1,400&display=swap">
<style>
  :root {
    --page: #ffffff;
    --midnight: #0f1626;
    --midnight-deep: #090e1a;
    --midnight-soft: #1b2538;
    --gold-dark: #c9a35a;
    --gold-light: #f3d79a;
    --gold-mid: #deb46a;
    --gold-shadow: #7a5c2c;
    --ivory: #ffffff;
    --ink: #141a28;
  }
  * { margin: 0; padding: 0; box-sizing: border-box; }
  html, body {
    width: 1200px;
    height: 1200px;
    overflow: hidden;
    background: var(--page);
  }
  .canvas {
    position: relative;
    width: 1200px;
    height: 1200px;
  }
  .cover {
    position: absolute;
    left: 240px;
    top: 60px;
    width: 720px;
    height: 1080px;
    overflow: hidden;
    background: var(--midnight);
    font-family: "EB Garamond", Georgia, serif;
  }
  .cover-texture {
    position: absolute;
    inset: 0;
    background: radial-gradient(ellipse at 50% 45%, var(--midnight-soft) 0%, var(--midnight) 55%, var(--midnight-deep) 100%);
  }
  .title,
  .subtitle,
  .tagline {
    position: absolute;
    left: 0;
    right: 0;
    text-align: center;
    white-space: nowrap;
    line-height: 1;
  }
  .title {
    top: 42px;
    font-size: 158px;
    font-weight: 500;
    letter-spacing: 2px;
    background: linear-gradient(180deg, var(--gold-dark) 0%, var(--gold-light) 55%, var(--gold-mid) 100%);
    -webkit-background-clip: text;
    background-clip: text;
    color: transparent;
  }
  .subtitle {
    top: 220px;
    color: var(--ivory);
    font-size: 66px;
    font-weight: 400;
    letter-spacing: 7px;
    word-spacing: 4px;
  }
  .emblem {
    position: absolute;
    left: 203px;
    top: 292px;
    width: 313px;
    height: 586px;
  }
  .emblem svg {
    display: block;
    width: 100%;
    height: 100%;
  }
  .tagline {
    top: 904px;
    color: var(--ivory);
    font-size: 50px;
    font-style: italic;
    font-weight: 400;
    letter-spacing: 2px;
  }
  .author-band {
    position: absolute;
    left: 0;
    right: 0;
    bottom: 0;
    height: 94px;
    background: linear-gradient(180deg, var(--gold-dark) 0%, var(--gold-light) 50%, var(--gold-dark) 100%);
    display: flex;
    align-items: center;
    justify-content: center;
  }
  .author-name {
    color: var(--ink);
    font-size: 48px;
    font-weight: 400;
    letter-spacing: 9px;
    line-height: 1;
    padding-top: 4px;
    white-space: nowrap;
  }
</style>
</head>
<body>
  <div class="canvas">
    <div class="cover">
      <div class="cover-texture" role="img" aria-label="Dunkler mitternachtsblauer Hintergrund mit fein geprägtem floralem Arabeskenmuster"></div>
      <h1 class="title">ṢALĀH</h1>
      <p class="subtitle">Das Gebet im Islam</p>
      <div class="emblem" role="img" aria-label="Goldener ornamentaler Rahmen mit Bogenfenster, darin die arabische Kalligrafie صلاة in Gold auf Mitternachtsblau">
        <svg viewBox="0 0 313 586" aria-hidden="true">
          <defs>
            <linearGradient id="frame-gold" x1="0" y1="0" x2="1" y2="1">
              <stop offset="0" stop-color="#8a6a32"/>
              <stop offset="0.45" stop-color="#deb46a"/>
              <stop offset="1" stop-color="#6e5428"/>
            </linearGradient>
          </defs>
          <rect x="0" y="33" width="313" height="520" fill="url(#frame-gold)" stroke="#c9a35a" stroke-width="2"/>
          <path d="M156 0 L190 33 L122 33 Z" fill="url(#frame-gold)"/>
          <path d="M156 553 L190 553 L156 586 L122 553 Z" fill="url(#frame-gold)"/>
          <path d="M156 80 C200 80 215 120 240 130 L240 170 C255 175 262 190 262 210 L262 400 C262 420 255 435 240 440 L240 480 C215 490 200 530 156 530 C112 530 97 490 72 480 L72 440 C57 435 50 420 50 400 L50 210 C50 190 57 175 72 170 L72 130 C97 120 112 80 156 80 Z" fill="#0f1626" stroke="#c9a35a" stroke-width="2"/>
        </svg>
      </div>
      <p class="tagline">Ein Weg zur Nähe mit Allah</p>
      <div class="author-band">
        <span class="author-name">AURHOR NAME</span>
      </div>
    </div>
  </div>
</body>
</html>
```